Business Card Design for Vantor Gear

We want to have a business card design for our company.
Company website: www.vantorgear-example.com.au
We looking for something cool, funky, and impressive, yet elegant.
Below are the contents that should be displayed on the card:
Front:
Name: Mark Dellow
Title: Sales & Purchasing
Company Name: Vantor Gear Pty Ltd
Phone: 02 5550 1473
Mobile: 0400 555 019
Email: mark@vantorgear-example.com.au
Website: www.vantorgear-example.com.au
Address: 17 Brackley St
Carrowlea, NSW 2199
Back:
We buy sell new used Norvex and network equipment
• Huge Savings - save up to 95% off list prices
• Highest Reliability
• Comprehensive Warranty
• Fast delivery
• Large range of hardware in stock
Our logo can be downloaded at: www.vantorgear-example.com.au/logo.zip

```html
<!DOCTYPE html>
<html lang="en">
<head>
<meta charset="utf-8">
<title>Vantor Gear – Business Card</title>
<link rel="stylesheet" href="https://fonts.googleapis.com/css2?family=Open+Sans:wght@400;600;700&display=swap">
<style>
  :root {
    --page: #e9e6e1;
    --navy: #2f2f9a;
    --sky: #2ba6e1;
    --red: #e4322b;
    --amber: #f7c21c;
    --white: #ffffff;
    --paper: #f6f5f8;
  }
  * { margin: 0; padding: 0; box-sizing: border-box; }
  html, body {
    width: 1200px; height: 900px; overflow: hidden;
    background: var(--page);
    font-family: "Open Sans", Arial, sans-serif;
  }
  .sheet {
    position: relative; width: 1200px; height: 900px;
    display: flex; align-items: center; justify-content: center; gap: 40px;
  }
  .card {
    position: relative; width: 560px; height: 320px;
    background: var(--navy); overflow: hidden;
    box-shadow: 0 8px 24px rgba(0,0,0,.18);
  }
  .card-art { position: absolute; inset: 0; }

  /* back */
  .back-copy { position: absolute; left: 250px; top: 52px; right: 20px; color: var(--white); }
  .brand-title { font-size: 42px; font-weight: 600; color: var(--sky); line-height: 1; letter-spacing: -0.5px; white-space: nowrap; }
  .brand-tagline { font-size: 10px; color: var(--red); letter-spacing: 4.6px; text-transform: uppercase; margin-top: 8px; white-space: nowrap; }
  .pitch { font-size: 11px; margin-top: 26px; line-height: 1.5; }
  .benefits { list-style: none; font-size: 11px; line-height: 1.5; }
  .benefits li::before { content: "• "; }

  /* front */
  .contact { position: absolute; left: 250px; top: 26px; color: var(--white); font-size: 12.5px; line-height: 1.5; }
  .contact-name { font-size: 22px; font-weight: 600; color: var(--sky); line-height: 1.2; }
  .contact-company { font-size: 17px; font-weight: 600; color: var(--sky); margin: 4px 0 6px; line-height: 1.2; }
  .label { color: var(--red); font-weight: 600; }
  .address { position: absolute; left: 330px; top: 240px; color: var(--white); font-size: 12.5px; line-height: 1.5; font-style: normal; }
  .logo-lockup { position: absolute; left: 30px; top: 240px; display: flex; align-items: center; gap: 8px; }
  .logo-dot { width: 30px; height: 30px; border-radius: 50%; background: var(--red); }
  .logo-name { font-size: 22px; font-weight: 700; color: var(--navy); line-height: 1; white-space: nowrap; }
</style>
</head>
<body>
<main class="sheet">

  <section class="card card-back" aria-label="Card back">
    <svg class="card-art" width="560" height="320" viewBox="0 0 560 320" aria-hidden="true">
      <circle cx="40" cy="310" r="195" fill="var(--red)"/>
    </svg>
    <div class="back-copy">
      <h1 class="brand-title">Vantor Gear</h1>
      <p class="brand-tagline">Networking Equipment</p>
      <p class="pitch">We buy sell new used Norvex and network equipment</p>
      <ul class="benefits">
        <li>Huge Savings - save up to 95% off list prices</li>
        <li>Highest Reliability</li>
        <li>Comprehensive Warranty</li>
        <li>Fast delivery</li>
        <li>Large range of hardware in stock</li>
      </ul>
    </div>
  </section>

  <section class="card card-front" aria-label="Card front">
    <svg class="card-art" width="560" height="320" viewBox="0 0 560 320" aria-hidden="true">
      <circle cx="60" cy="345" r="236" fill="var(--amber)"/>
      <circle cx="60" cy="345" r="230" fill="var(--red)"/>
      <circle cx="60" cy="345" r="224" fill="var(--paper)"/>
    </svg>
    <div class="contact">
      <p class="contact-name">Mark Dellow</p>
      <p class="contact-title">Sales &amp; Purchasing</p>
      <p class="contact-company">Vantor Gear Pty Ltd</p>
      <p><span class="label">p:</span> 02 5550 1473</p>
      <p><span class="label">m:</span> 0400 555 019</p>
      <p><span class="label">e:</span> mark@vantorgear-example.com.au</p>
      <p><span class="label">w:</span> www.vantorgear-example.com.au</p>
    </div>
    <address class="address">
      Address: 17 Brackley St<br>Carrowlea, NSW 2199
    </address>
    <div class="logo-lockup">
      <span class="logo-dot" aria-hidden="true"></span>
      <span class="logo-name">Vantor Gear</span>
    </div>
  </section>

</main>
</body>
</html>
```